Power Point CI

Creat a Slide Master which we can use and also add new slides with bullets, or other graphic design which we can fill. Power Point Master Format - also amend the graphics on the PPT - especially the project roadmap or profile page. have a look on our website www.brightlantern.io. I would also appreciate other slides which we can use and fill

Target Market(s)

companies - PE, HR Executive

Industry/Entity Type

Executive Search

Font styles to use
Serif
Other font styles liked:
• Calibri or Coast like on our website

Colors
0094D4
00A9DD
6FCCEA
C7EBF8
E9F6FB

Requirements
Must have
• needs to sleek and slim - prefer white and bright elegant Backgrounds
Nice to have
• it should somehow fit to our website and corporate CI
Should not have
• Full green CI

```html
<!DOCTYPE html>
<html lang="en">
<head>
<meta charset="utf-8">
<title>Bright Lantern – Slide Master</title>
<link href="https://fonts.googleapis.com/css2?family=Oswald:wght@300;400;500&family=Open+Sans:wght@400;600;700&display=swap" rel="stylesheet">
<style>
:root{
  --blue-strong:#0094D4;
  --blue:#00A9DD;
  --blue-mid:#6FCCEA;
  --blue-light:#C7EBF8;
  --blue-pale:#E9F6FB;
  --petrol-dark:#0c3b4d;
  --petrol:#1b6a80;
  --ink:#2b2f33;
  --text:#6b7278;
  --rule:#d9dde0;
  --accent-red:#e0413a;
  --orange:#f39a1e;
  --green:#8cc63f;
  --red:#e8503a;
  --page:#ffffff;
}
*{box-sizing:border-box;margin:0;padding:0}
html,body{width:1200px;height:2416px;overflow:hidden;background:var(--page)}
body{position:relative;font-family:"Open Sans",Arial,sans-serif;color:var(--text)}
.slide{position:absolute;width:552px;height:310px;background:#fff;box-shadow:0 1px 4px rgba(0,0,0,.18);overflow:hidden}
.col-l{left:24px}.col-r{left:624px}
.cover{background:linear-gradient(135deg,var(--petrol-dark) 0%,var(--petrol) 55%,#0f4f63 100%)}
.cover .facets{position:absolute;inset:0}
.brand-title{position:absolute;left:0;right:0;top:128px;text-align:center;font-family:"Oswald",sans-serif;font-weight:300;color:#fff;font-size:36px;letter-spacing:3px}
.brand-tag{position:absolute;left:0;right:0;top:178px;text-align:center;color:var(--blue-light);font-size:9px;letter-spacing:3px}
.accent-bar{position:absolute;left:0;top:22px;width:4px;height:120px;background:var(--accent-red)}
.mini-brand{position:absolute;left:16px;top:14px;font-family:"Oswald",sans-serif;font-size:8px;letter-spacing:1.5px;color:var(--blue-mid)}
.slide-title{position:absolute;left:20px;font-family:"Oswald",sans-serif;font-weight:500;color:var(--ink);font-size:17px;line-height:1.2;width:150px}
.body{position:absolute;font-size:6.5px;line-height:1.55;color:var(--text)}
.body p{margin-bottom:6px}
.photo{position:absolute;background:linear-gradient(160deg,#d6d9dc,#8e959b)}
.bullets{list-style:none}
.bullets li{position:relative;padding-left:13px;margin-bottom:9px}
.bullets li::before{content:"";position:absolute;left:0;top:2px;width:7px;height:7px;background:var(--blue)}
.value{position:absolute;width:170px;height:120px}
.value .tile{position:absolute;left:0;top:0;width:40px;height:40px}
.value h4{position:absolute;left:48px;top:4px;font-family:"Oswald",sans-serif;font-weight:500;font-size:9px;letter-spacing:.5px;color:var(--ink)}
.value .body{left:48px;top:20px;width:118px}
table.refs{position:absolute;left:200px;top:40px;width:330px;border-collapse:collapse;font-size:6.5px}
.refs th{background:var(--blue-strong);color:#fff;text-align:left;padding:5px 6px;font-weight:600}
.refs td{padding:6px;border-bottom:1px solid var(--rule)}
.refs tr:nth-child(even) td{background:var(--blue-pale)}
.num{position:absolute;width:22px;height:22px;border-radius:50%;color:#fff;font-size:9px;font-weight:700;text-align:center;line-height:22px}
.item-label{position:absolute;font-family:"Oswald",sans-serif;font-size:8px;color:var(--ink)}
.profile-card{position:absolute;width:100px;height:80px;background:linear-gradient(180deg,var(--blue-pale),var(--blue-light));border:1px solid var(--rule)}
.phase{position:absolute;text-align:center;width:70px;font-family:"Oswald",sans-serif;font-size:7px;color:var(--ink)}
.step{position:absolute;width:38px;height:38px;border-radius:50%;border:4px solid;background:#fff;text-align:center;line-height:30px;font-family:"Oswald",sans-serif;font-size:13px;color:var(--ink)}
.gantt-label{position:absolute;font-size:6px;color:var(--text)}
.bar{position:absolute;height:7px}
.social{position:absolute;width:12px;height:12px;border-radius:50%;background:var(--blue-mid)}
</style>
</head>
<body>

<!-- 1 Cover -->
<section class="slide col-l cover" style="top:20px">
  <svg class="facets" viewBox="0 0 552 310" aria-hidden="true"><polygon points="0,310 230,120 552,310" fill="#ffffff" opacity=".04"/><polygon points="300,0 552,0 552,200" fill="#ffffff" opacity=".05"/></svg>
  <div class="brand-title">BRIGHT LANTERN</div>
  <div class="brand-tag">CLEAR | TRUSTED | FOCUSED | LASTING</div>
</section>

<!-- 2 Consultant profile -->
<section class="slide col-r" style="top:20px">
  <div class="mini-brand">BRIGHT LANTERN</div>
  <div class="accent-bar"></div>
  <div class="slide-title" style="top:150px;width:140px">Dr. Clara Weidmann-Lorenz</div>
  <div class="photo" role="img" aria-label="Portrait photo of the consultant" style="left:170px;top:60px;width:110px;height:140px"></div>
  <div class="body" style="left:300px;top:50px;width:225px">
    <p>Partner with over twenty years of experience in executive search for private equity portfolios and family-owned industrial groups across Europe.</p>
    <p>Former HR leader in an international consumer goods company, responsible for talent strategy and leadership development.</p>
    <p>Focus on board, managing director and functional C-level mandates. Fluent in German, English and French.</p>
  </div>
</section>

<!-- 3 Consultant profile -->
<section class="slide col-l" style="top:362px">
  <div class="mini-brand">BRIGHT LANTERN</div>
  <div class="accent-bar"></div>
  <div class="photo" role="img" aria-label="Portrait photo of the consultant" style="left:120px;top:40px;width:110px;height:140px"></div>
  <div class="slide-title" style="top:205px">Marie Ostendorf</div>
  <div class="body" style="left:290px;top:50px;width:235px">
    <p>Senior consultant specialising in finance, HR and operations roles for mid-cap companies and their investors.</p>
    <p>Background in strategy consulting and corporate finance; guides clients from briefing to onboarding.</p>
    <p>Known for structured assessments and a trusted network across the DACH region.</p>
  </div>
</section>

<!-- 4 Who we are -->
<section class="slide col-r" style="top:362px">
  <div class="mini-brand">BRIGHT LANTERN</div>
  <div class="accent-bar"></div>
  <div class="slide-title" style="top:130px">Who We Are and How We Work</div>
  <ul class="body bullets" style="left:190px;top:50px;width:160px">
    <li>Independent boutique for executive search with a clear partner focus.</li>
    <li>Every mandate is led personally from start to finish.</li>
    <li>Research based on market mapping and direct approach.</li>
    <li>Transparent reporting at each stage.</li>
  </ul>
  <ul class="body bullets" style="left:370px;top:50px;width:160px">
    <li>Deep expertise in private equity and portfolio companies.</li>
    <li>Strong network of senior HR executives.</li>
    <li>Structured interviews and reference checks.</li>
  </ul>
</section>

<!-- 5 Values -->
<section class="slide col-l" style="top:704px">
  <div class="mini-brand">BRIGHT LANTERN</div>
  <div class="accent-bar"></div>
  <div class="slide-title" style="top:140px">Our Values</div>
  <div class="value" style="left:180px;top:40px"><div class="tile" style="background:var(--orange)"></div><h4>HONESTY</h4><div class="body">We give clear, candid advice to clients and candidates alike.</div></div>
  <div class="value" style="left:365px;top:40px"><div class="tile" style="background:var(--green)"></div><h4>PROGRESS</h4><div class="body">We keep searches moving with a steady and visible pace.</div></div>
  <div class="value" style="left:180px;top:170px"><div class="tile" style="background:var(--red)"></div><h4>PERSONAL</h4><div class="body">Partners lead each mandate and stay close to every client.</div></div>
  <div class="value" style="left:365px;top:170px"><div class="tile" style="background:var(--blue)"></div><h4>DIVERSE</h4><div class="body">We open shortlists to fresh profiles and broad perspectives.</div></div>
</section>

<!-- 6 References -->
<section class="slide col-r" style="top:704px">
  <div class="mini-brand">BRIGHT LANTERN</div>
  <div class="accent-bar"></div>
  <div class="slide-title" style="top:120px">Relevant Reference Assignments (excerpt)</div>
  <table class="refs">
    <tr><th>Position</th><th>Client</th><th>Year</th></tr>
    <tr><td>Chief Financial Officer</td><td>PE-backed industrial group</td><td>2023</td></tr>
    <tr><td>Managing Director</td><td>Medical technology</td><td>2023</td></tr>
    <tr><td>Chief HR Officer</td><td>Consumer goods</td><td>2022</td></tr>
    <tr><td>Head of Operations</td><td>Logistics services</td><td>2022</td></tr>
    <tr><td>Chief Executive Officer</td><td>Software portfolio</td><td>2021</td></tr>
  </table>
</section>

<!-- 7 Target universe -->
<section class="slide col-l" style="top:1046px">
  <div class="mini-brand">BRIGHT LANTERN</div>
  <div class="accent-bar"></div>
  <div class="slide-title" style="top:140px">Target Universe</div>
  <div class="num" style="left:180px;top:50px;background:var(--blue-strong)">1</div>
  <div class="num" style="left:180px;top:110px;background:var(--blue)">2</div>
  <div class="num" style="left:180px;top:170px;background:var(--blue-mid)">3</div>
  <div class="num" style="left:180px;top:230px;background:var(--orange)">4</div>
  <div class="item-label" style="left:210px;top:48px">Direct competitors</div><div class="body" style="left:210px;top:62px;width:150px">Companies in the same segment and region.</div>
  <div class="item-label" style="left:210px;top:108px">Adjacent industries</div><div class="body" style="left:210px;top:122px;width:150px">Firms with similar products or channels.</div>
  <div class="item-label" style="left:210px;top:168px">PE portfolios</div><div class="body" style="left:210px;top:182px;width:150px">Comparable investor-owned businesses.</div>
  <div class="item-label" style="left:210px;top:228px">Advisory firms</div><div class="body" style="left:210px;top:242px;width:150px">Consultants with relevant sector focus.</div>
  <svg style="position:absolute;right:0;top:20px" width="160" height="270" viewBox="0 0 160 270" aria-hidden="true">
    <circle cx="160" cy="135" r="135" fill="var(--blue-strong)"/>
    <circle cx="160" cy="135" r="105" fill="var(--blue)"/>
    <circle cx="160" cy="135" r="75" fill="var(--blue-mid)"/>
    <circle cx="160" cy="135" r="45" fill="var(--orange)"/>
  </svg>
</section>

<!-- 8 Candidate profile wheel -->
<section class="slide col-r" style="top:1046px">
  <div class="mini-brand">BRIGHT LANTERN</div>
  <div class="accent-bar"></div>
  <div class="slide-title" style="top:150px">Candidate Profile – for discussion</div>
  <div class="body" style="left:180px;top:60px;width:90px">Proven P&amp;L responsibility in a mid-cap environment.</div>
  <div class="body" style="left:180px;top:180px;width:90px">Experience working with investors and boards.</div>
  <div class="body" style="left:450px;top:60px;width:90px">Hands-on leader who builds strong teams.</div>
  <div class="body" style="left:450px;top:180px;width:90px">International exposure and change agenda.</div>
  <svg style="position:absolute;left:285px;top:70px" width="160" height="160" viewBox="0 0 160 160" aria-hidden="true">
    <g stroke="var(--rule)" stroke-width="1"><line x1="80" y1="80" x2="80" y2="14"/><line x1="80" y1="80" x2="80" y2="146"/><line x1="80" y1="80" x2="14" y2="80"/><line x1="80" y1="80" x2="146" y2="80"/><line x1="80" y1="80" x2="33" y2="33"/><line x1="80" y1="80" x2="127" y2="127"/><line x1="80" y1="80" x2="127" y2="33"/><line x1="80" y1="80" x2="33" y2="127"/></g>
    <circle cx="80" cy="14" r="11" fill="var(--orange)"/><circle cx="127" cy="33" r="11" fill="var(--green)"/><circle cx="146" cy="80" r="11" fill="var(--blue)"/><circle cx="127" cy="127" r="11" fill="var(--red)"/><circle cx="80" cy="146" r="11" fill="var(--blue-strong)"/><circle cx="33" cy="127" r="11" fill="var(--blue-mid)"/><circle cx="14" cy="80" r="11" fill="var(--orange)"/><circle cx="33" cy="33" r="11" fill="var(--green)"/>
    <circle cx="80" cy="80" r="34" fill="var(--petrol)"/>
    <text x="80" y="76" text-anchor="middle" font-family="Oswald,sans-serif" font-size="7" fill="#fff">CORE OF</text>
    <text x="80" y="86" text-anchor="middle" font-family="Oswald,sans-serif" font-size="7" fill="#fff">RELEVANT SKILLS</text>
  </svg>
</section>

<!-- 9 Candidate profile cards -->
<section class="slide col-l" style="top:1388px">
  <div class="mini-brand">BRIGHT LANTERN</div>
  <div class="accent-bar"></div>
  <div class="slide-title" style="top:150px">Candidate Profile – for discussion</div>
  <div class="profile-card" role="img" aria-label="Candidate placeholder image" style="left:185px;top:40px"></div>
  <div class="profile-card" role="img" aria-label="Candidate placeholder image" style="left:300px;top:40px"></div>
  <div class="profile-card" role="img" aria-label="Candidate placeholder image" style="left:415px;top:40px"></div>
  <div class="body" style="left:185px;top:130px;width:100px">Candidate A: CFO, industrial group, 15 years experience.</div>
  <div class="body" style="left:300px;top:130px;width:100px">Candidate B: COO, services firm, strong turnaround record.</div>
  <div class="body" style="left:415px;top:130px;width:100px">Candidate C: CEO, PE portfolio, international scale-up.</div>
</section>

<!-- 10 Search process -->
<section class="slide col-r" style="top:1388px">
  <div class="mini-brand">BRIGHT LANTERN</div>
  <div class="accent-bar"></div>
  <div class="slide-title" style="top:140px">Search Process</div>
  <div class="phase" style="left:170px;top:30px">Phase I<br>Briefing</div>
  <div class="phase" style="left:305px;top:30px">Phase II<br>Research</div>
  <div class="phase" style="left:440px;top:30px">Phase III<br>Selection</div>
  <div style="position:absolute;left:200px;top:110px;width:310px;height:2px;background:var(--rule)"></div>
  <div class="step" style="left:181px;top:92px;border-color:var(--blue-strong)">1</div>
  <div class="step" style="left:250px;top:92px;border-color:var(--blue)">2</div>
  <div class="step" style="left:319px;top:92px;border-color:var(--blue-mid)">3</div>
  <div class="step" style="left:388px;top:92px;border-color:var(--green)">4</div>
  <div class="step" style="left:457px;top:92px;border-color:var(--orange)">5</div>
  <div class="body" style="left:170px;top:150px;width:60px;text-align:center">Kick-off and job profile</div>
  <div class="body" style="left:239px;top:150px;width:60px;text-align:center">Market mapping</div>
  <div class="body" style="left:308px;top:150px;width:60px;text-align:center">Direct approach</div>
  <div class="body" style="left:377px;top:150px;width:60px;text-align:center">Interviews and shortlist</div>
  <div class="body" style="left:446px;top:150px;width:60px;text-align:center">Offer and onboarding</div>
</section>

<!-- 11 Timeline -->
<section class="slide col-l" style="top:1730px">
  <div class="mini-brand">BRIGHT LANTERN</div>
  <div class="accent-bar"></div>
  <div class="slide-title" style="top:140px">Draft Project Timeline for placement</div>
  <div style="position:absolute;left:190px;top:40px;width:340px;height:14px;background:var(--blue-strong)"></div>
  <div class="gantt-label" style="left:196px;top:43px;color:#fff">Week 1 – 12</div>
  <div class="gantt-label" style="left:190px;top:70px">Briefing</div><div class="bar" style="left:270px;top:70px;width:40px;background:var(--blue)"></div>
  <div class="gantt-label" style="left:190px;top:90px">Research</div><div class="bar" style="left:300px;top:90px;width:80px;background:var(--blue-mid)"></div>
  <div class="gantt-label" style="left:190px;top:110px">Approach</div><div class="bar" style="left:330px;top:110px;width:90px;background:var(--blue)"></div>
  <div class="gantt-label" style="left:190px;top:130px">Interviews</div><div class="bar" style="left:390px;top:130px;width:70px;background:var(--green)"></div>
  <div class="gantt-label" style="left:190px;top:150px">Shortlist</div><div class="bar" style="left:440px;top:150px;width:40px;background:var(--orange)"></div>
  <div class="gantt-label" style="left:190px;top:170px">Offer</div><div class="bar" style="left:475px;top:170px;width:45px;background:var(--red)"></div>
  <div style="position:absolute;left:190px;top:200px;width:340px;height:8px;background:var(--blue-pale)"></div>
  <div class="gantt-label" style="left:270px;top:212px">Month 1</div><div class="gantt-label" style="left:370px;top:212px">Month 2</div><div class="gantt-label" style="left:470px;top:212px">Month 3</div>
</section>

<!-- 12 Digital tool -->
<section class="slide col-r" style="top:1730px">
  <div class="mini-brand">BRIGHT LANTERN</div>
  <div class="accent-bar"></div>
  <div class="slide-title" style="top:130px">Digital Tool for Full Transparency</div>
  <div role="img" aria-label="Screenshot of the online candidate tracking tool" style="position:absolute;left:180px;top:50px;width:190px;height:190px;background:linear-gradient(180deg,#f4f6f8,#dfe4e8);border:1px solid var(--rule)"></div>
  <div style="position:absolute;left:385px;top:50px;width:70px;height:60px;background:var(--orange)"></div>
  <div style="position:absolute;left:462px;top:50px;width:70px;height:60px;background:var(--green)"></div>
  <div style="position:absolute;left:385px;top:117px;width:70px;height:60px;background:var(--blue)"></div>
  <div style="position:absolute;left:462px;top:117px;width:70px;height:60px;background:var(--red)"></div>
  <div class="body" style="left:385px;top:190px;width:145px">Clients follow every candidate and status update online, at any time.</div>
</section>

<!-- 13 Closing -->
<section class="slide col-l cover" style="top:2072px">
  <div class="brand-title" style="top:120px;font-size:30px">BRIGHT LANTERN</div>
  <div class="brand-tag" style="top:166px">www.brightlantern.io</div>
  <div class="social" style="left:470px;top:280px"></div>
  <div class="social" style="left:488px;top:280px"></div>
  <div class="social" style="left:506px;top:280px"></div>
</section>

</body>
</html>
```